Beekeeper needs box/label design for honey/CBD and other honey-related products

We need a box (or label) design for a beekeeping company in Virginia called Larkmoor Hollow Farm. Our products will include honey mixed with CBD oil and other essential oils (vanilla, lavender, etc).The box design should be scalable to include several different honey/oil products. We would like to incorporate our current farm logo into the design. Here is a link to a honey producing company with a series of products using their honey mixed with certain oils. It's a good reference of what type box/label design we would like (https://pipandwrenly.co/pages/honey).

Target Market(s)

Retail stores and consumers

Requirements
Must have
• Larkmoor Hollow Farm name and logo

```html
<!DOCTYPE html>
<html lang="en">
<head>
<meta charset="utf-8">
<title>Larkmoor Hollow Farm — Raw Honey Packaging</title>
<link href="https://fonts.googleapis.com/css2?family=Lato:wght@400;700;900&display=swap" rel="stylesheet">
<style>
:root{
  --canvas:#ececec;
  --paper:#ffffff;
  --ink:#333333;
  --body-ink:#555555;
  --brand:#8a9a2a;
  --edge:#d6d6d6;
  --blueberry:#6f6ab0;
  --blueberry-soft:#b9b5de;
  --lavender:#8a5c9e;
  --lavender-soft:#c9abd3;
  --raspberry:#d4467c;
  --raspberry-soft:#eca6c1;
}
*{margin:0;padding:0;box-sizing:border-box}
html,body{width:1200px;height:3563px;overflow:hidden;background:var(--canvas)}
body{font-family:"Lato",sans-serif;color:var(--ink)}
.variant{position:relative;width:1200px;height:1187px}
.variant--blueberry{--accent:var(--blueberry);--accent-soft:var(--blueberry-soft)}
.variant--lavender{--accent:var(--lavender);--accent-soft:var(--lavender-soft)}
.variant--raspberry{--accent:var(--raspberry);--accent-soft:var(--raspberry-soft)}

.face{position:absolute;top:360px;width:330px;height:460px;background:var(--paper);border:1px solid var(--edge);overflow:hidden}
.face--side{left:90px}
.face--front{left:419px}
.label{position:absolute;top:360px;left:790px;width:320px;height:460px;background:var(--paper);border:1px solid var(--edge);border-radius:6px;overflow:hidden}

.brand{position:absolute;left:0;right:0;text-align:center;color:var(--brand);font-weight:700;font-size:15px;letter-spacing:2px;line-height:1.2}
.brand__mark{display:block;width:38px;height:38px;margin:0 auto 8px;background:var(--brand)}
.face--front .brand,.label .brand{top:34px}

.initial{position:absolute;font-weight:400;color:var(--accent-soft);opacity:.85;line-height:1}
.face--front .initial,.label .initial{left:40px;top:150px;font-size:190px}

.title{position:absolute;font-size:25px;font-weight:400;color:var(--ink);letter-spacing:.5px}
.flavour{position:absolute;font-size:9.5px;font-weight:900;letter-spacing:1px;color:var(--accent);text-transform:uppercase}
.face--front .title,.label .title{left:120px;top:200px}
.face--front .flavour,.label .flavour{left:100px;top:236px}

.copy{position:absolute;font-size:9px;line-height:1.45;color:var(--body-ink);text-align:justify}
.face--front .copy,.label .copy{left:108px;right:30px;top:270px}
.net{position:absolute;left:0;right:0;bottom:34px;text-align:center;font-size:8.5px;color:var(--body-ink);letter-spacing:.5px}

.face--side .title{left:0;right:0;top:30px;text-align:center;font-size:21px}
.face--side .flavour{left:0;right:0;top:60px;text-align:center;font-size:8.5px}
.face--side .copy{left:26px;right:26px}
.face--side .copy--one{top:90px}
.face--side .copy--two{top:190px}
.side-brand{position:absolute;left:26px;top:270px;color:var(--brand);font-weight:700;font-size:11px;letter-spacing:1px;line-height:1.3;width:120px}
.side-brand__mark{display:block;width:20px;height:20px;margin-bottom:6px;background:var(--brand)}
.address{position:absolute;left:26px;top:330px;font-size:9px;line-height:1.5;color:var(--body-ink)}
</style>
</head>
<body>

<section class="variant variant--blueberry" aria-label="Raw honey, wildflower with blueberry">
  <div class="face face--side">
    <h2 class="title">RAW HONEY</h2>
    <p class="flavour">Wildflower with Blueberry</p>
    <p class="copy copy--one">Lorem ipsum dolor sit amet, consectetuer adipiscing elit, sed diam nonummy nibh euismod tincidunt ut laoreet dolore magna aliquam erat volutpat. Ut wisi enim ad minim veniam, quis nostrud exerci tation ullamcorper suscipit lobortis nisl ut aliquip ex ea commodo consequat.</p>
    <p class="copy copy--two">Lorem ipsum dolor sit amet, consectetuer adipiscing elit, sed diam nonummy nibh euismod tincidunt ut laoreet dolore magna aliquam.</p>
    <div class="side-brand"><span class="side-brand__mark"></span>LARKMOOR HOLLOW FARM</div>
    <p class="address">1840 Clover Ridge Road<br>Staunton, Virginia 24401<br>United States</p>
  </div>
  <div class="face face--front">
    <div class="brand"><span class="brand__mark"></span>LARKMOOR HOLLOW<br>FARM</div>
    <span class="initial">B</span>
    <h2 class="title">RAW HONEY</h2>
    <p class="flavour">Wildflower with Blueberry</p>
    <p class="copy">Lorem ipsum dolor sit amet, consectetuer adipiscing elit, sed diam nonummy nibh euismod tincidunt ut laoreet dolore magna aliquam erat volutpat. Ut wisi enim ad minim veniam, quis nostrud exerci tation ullamcorper suscipit lobortis nisl ut aliquip ex ea commodo consequat. Duis autem accumsan et iusto odio.</p>
    <p class="net">NET WT. 16 OUNCES (454 GRAMS)</p>
  </div>
  <div class="label">
    <div class="brand"><span class="brand__mark"></span>LARKMOOR HOLLOW<br>FARM</div>
    <span class="initial">B</span>
    <h2 class="title">RAW HONEY</h2>
    <p class="flavour">Wildflower with Blueberry</p>
    <p class="copy">Lorem ipsum dolor sit amet, consectetuer adipiscing elit, sed diam nonummy nibh euismod tincidunt ut laoreet dolore magna aliquam erat volutpat. Ut wisi enim ad minim veniam, quis nostrud exerci tation ullamcorper suscipit lobortis nisl ut aliquip ex ea commodo consequat. Duis autem accumsan et iusto odio.</p>
    <p class="net">NET WT. 16 OUNCES (454 GRAMS)</p>
  </div>
</section>

<section class="variant variant--lavender" aria-label="Raw honey, wildflower with lavender">
  <div class="face face--side">
    <h2 class="title">RAW HONEY</h2>
    <p class="flavour">Wildflower with Lavender</p>
    <p class="copy copy--one">Lorem ipsum dolor sit amet, consectetuer adipiscing elit, sed diam nonummy nibh euismod tincidunt ut laoreet dolore magna aliquam erat volutpat. Ut wisi enim ad minim veniam, quis nostrud exerci tation ullamcorper suscipit lobortis nisl ut aliquip ex ea commodo consequat.</p>
    <p class="copy copy--two">Lorem ipsum dolor sit amet, consectetuer adipiscing elit, sed diam nonummy nibh euismod tincidunt ut laoreet dolore magna aliquam.</p>
    <div class="side-brand"><span class="side-brand__mark"></span>LARKMOOR HOLLOW FARM</div>
    <p class="address">1840 Clover Ridge Road<br>Staunton, Virginia 24401<br>United States</p>
  </div>
  <div class="face face--front">
    <div class="brand"><span class="brand__mark"></span>LARKMOOR HOLLOW<br>FARM</div>
    <span class="initial">L</span>
    <h2 class="title">RAW HONEY</h2>
    <p class="flavour">Wildflower with Lavender</p>
    <p class="copy">Lorem ipsum dolor sit amet, consectetuer adipiscing elit, sed diam nonummy nibh euismod tincidunt ut laoreet dolore magna aliquam erat volutpat. Ut wisi enim ad minim veniam, quis nostrud exerci tation ullamcorper suscipit lobortis nisl ut aliquip ex ea commodo consequat. Duis autem accumsan et iusto odio.</p>
    <p class="net">NET WT. 16 OUNCES (454 GRAMS)</p>
  </div>
  <div class="label">
    <div class="brand"><span class="brand__mark"></span>LARKMOOR HOLLOW<br>FARM</div>
    <span class="initial">L</span>
    <h2 class="title">RAW HONEY</h2>
    <p class="flavour">Wildflower with Lavender</p>
    <p class="copy">Lorem ipsum dolor sit amet, consectetuer adipiscing elit, sed diam nonummy nibh euismod tincidunt ut laoreet dolore magna aliquam erat volutpat. Ut wisi enim ad minim veniam, quis nostrud exerci tation ullamcorper suscipit lobortis nisl ut aliquip ex ea commodo consequat. Duis autem accumsan et iusto odio.</p>
    <p class="net">NET WT. 16 OUNCES (454 GRAMS)</p>
  </div>
</section>

<section class="variant variant--raspberry" aria-label="Raw honey, wildflower with raspberry">
  <div class="face face--side">
    <h2 class="title">RAW HONEY</h2>
    <p class="flavour">Wildflower with Raspberry</p>
    <p class="copy copy--one">Lorem ipsum dolor sit amet, consectetuer adipiscing elit, sed diam nonummy nibh euismod tincidunt ut laoreet dolore magna aliquam erat volutpat. Ut wisi enim ad minim veniam, quis nostrud exerci tation ullamcorper suscipit lobortis nisl ut aliquip ex ea commodo consequat.</p>
    <p class="copy copy--two">Lorem ipsum dolor sit amet, consectetuer adipiscing elit, sed diam nonummy nibh euismod tincidunt ut laoreet dolore magna aliquam.</p>
    <div class="side-brand"><span class="side-brand__mark"></span>LARKMOOR HOLLOW FARM</div>
    <p class="address">1840 Clover Ridge Road<br>Staunton, Virginia 24401<br>United States</p>
  </div>
  <div class="face face--front">
    <div class="brand"><span class="brand__mark"></span>LARKMOOR HOLLOW<br>FARM</div>
    <span class="initial">R</span>
    <h2 class="title">RAW HONEY</h2>
    <p class="flavour">Wildflower with Raspberry</p>
    <p class="copy">Lorem ipsum dolor sit amet, consectetuer adipiscing elit, sed diam nonummy nibh euismod tincidunt ut laoreet dolore magna aliquam erat volutpat. Ut wisi enim ad minim veniam, quis nostrud exerci tation ullamcorper suscipit lobortis nisl ut aliquip ex ea commodo consequat. Duis autem accumsan et iusto odio.</p>
    <p class="net">NET WT. 16 OUNCES (454 GRAMS)</p>
  </div>
  <div class="label">
    <div class="brand"><span class="brand__mark"></span>LARKMOOR HOLLOW<br>FARM</div>
    <span class="initial">R</span>
    <h2 class="title">RAW HONEY</h2>
    <p class="flavour">Wildflower with Raspberry</p>
    <p class="copy">Lorem ipsum dolor sit amet, consectetuer adipiscing elit, sed diam nonummy nibh euismod tincidunt ut laoreet dolore magna aliquam erat volutpat. Ut wisi enim ad minim veniam, quis nostrud exerci tation ullamcorper suscipit lobortis nisl ut aliquip ex ea commodo consequat. Duis autem accumsan et iusto odio.</p>
    <p class="net">NET WT. 16 OUNCES (454 GRAMS)</p>
  </div>
</section>

</body>
</html>
```